National Training and assessment company needs a website

Create a 4 page website, simple but professional, the company provides training services to industry, resumes'/ CVs, personnel skill assessment, workplace skills profiling and develops manufactures and supplies training equipment for electrical/engineering training, Company title is Corvan T Pty Ltd and also trades under RSK & Associates. letterheads etc all are done using dark green
Updates
Project Deadline Extended
Reason: Due to work commitments will be interstate from the 26/02 til 05/03/14
Target Market(s)
The market is broad covering the general public, secondary colleges and corporate sector
Industry/Entity Type
Training
Look and feel
Each slider illustrates characteristics of the customer's brand and the style your logo design should communicate.

```html
<!DOCTYPE html>
<html lang="en">
<head>
<meta charset="utf-8">
<title>Corvan T Pty Ltd — RSK &amp; Associates</title>
<link rel="stylesheet" href="https://fonts.googleapis.com/css2?family=Gelasio&family=Open+Sans:wght@400&family=Arimo&display=swap">
<style>
  :root {
    --brand-green: #174d45;
    --header-black: #000000;
    --text-green: #1f4f48;
    --accent-green: #78b548;
    --soft-green: #9ccb7c;
    --search-field: #cfdcdb;
    --white: #ffffff;
    --hero-top: #5a4a9a;
    --hero-mid: #9a7bc9;
    --hero-low: #d9a9c0;
    --hero-glow: #f08a3a;
  }
  * { margin: 0; padding: 0; box-sizing: border-box; }
  html, body { width: 1179px; height: 1200px; overflow: hidden; background: var(--white); }
  .page { position: relative; width: 1179px; height: 1200px; overflow: hidden; font-family: "Open Sans", sans-serif; }

  .top-band { position: absolute; left: 0; top: 0; width: 100%; height: 32px; background: var(--brand-green); }

  .site-header { position: absolute; left: 0; top: 32px; width: 100%; height: 197px; background: var(--header-black); }
  .brand { position: absolute; left: 50px; top: 60px; color: var(--white); }
  .brand-name { font-family: "Gelasio", serif; font-size: 56px; line-height: 1; letter-spacing: 0.2px; }
  .brand-trade { font-family: "Arimo", sans-serif; font-size: 19px; line-height: 1; margin-top: 1px; }

  .search { position: absolute; left: 546px; top: 40px; display: flex; gap: 12px; }
  .search-field { width: 382px; height: 46px; background: var(--search-field); border: 3px solid var(--brand-green); border-radius: 4px; }
  .search-button { width: 189px; height: 47px; border-radius: 4px; border: 0;
    background: linear-gradient(to bottom, #7fa39d 0, #7fa39d 38%, var(--brand-green) 38%);
    color: var(--white); font-family: "Open Sans", sans-serif; font-size: 20px; letter-spacing: 0.5px;
    display: flex; align-items: center; justify-content: center; gap: 10px; }

  .main-nav { position: absolute; right: 50px; top: 138px; display: flex; gap: 16px; }
  .main-nav a { color: var(--white); text-decoration: none; font-size: 15px; letter-spacing: 0.2px; }

  .hero { position: absolute; left: 0; top: 229px; width: 100%; height: 543px;
    background: linear-gradient(to bottom, var(--hero-top) 0%, var(--hero-mid) 45%, var(--hero-low) 75%, var(--hero-glow) 92%, #3a2230 100%); }
  .hero-line { position: absolute; color: var(--white); font-family: "Gelasio", serif; font-size: 28px; line-height: 1; }
  .hero-line.first { left: 50px; top: 50px; }
  .hero-line.second { left: 158px; top: 80px; }

  .intro { position: absolute; left: 50px; top: 819px; color: var(--text-green); font-size: 14px; line-height: 22.4px; }
  .intro ul { list-style: none; }
  .intro li::before { content: "·"; margin-right: 6px; }

  .divider { position: absolute; left: 768px; top: 825px; width: 1px; height: 275px; background: var(--accent-green); }

  .contact { position: absolute; left: 792px; top: 818px; }
  .contact-name { font-family: "Gelasio", serif; font-size: 40px; line-height: 1; color: var(--accent-green); }
  .contact-trade { font-family: "Arimo", sans-serif; font-size: 14px; color: var(--accent-green); margin-top: 0; }
  .contact-details { margin-top: 10px; font-size: 14px; line-height: 20.6px; color: var(--soft-green); font-style: normal; }

  .site-footer { position: absolute; left: 0; top: 1155px; width: 100%; height: 45px; background: var(--brand-green);
    display: flex; justify-content: center; align-items: center; }
</style>
</head>
<body>
<div class="page">
  <div class="top-band"></div>

  <header class="site-header">
    <div class="brand">
      <div class="brand-name">Corvan T Pty Ltd</div>
      <div class="brand-trade">RSK &amp; Associates</div>
    </div>

    <div class="search">
      <div class="search-field"></div>
      <div class="search-button">
        <svg width="30" height="30" viewBox="0 0 30 30" aria-hidden="true">
          <circle cx="15" cy="15" r="13" fill="none" stroke="#fff" stroke-width="2"/>
          <circle cx="13.5" cy="13.5" r="5" fill="none" stroke="#fff" stroke-width="2"/>
          <line x1="17" y1="17" x2="21" y2="21" stroke="#fff" stroke-width="2.4" stroke-linecap="round"/>
        </svg>
        <span>SEARCH</span>
      </div>
    </div>

    <nav class="main-nav">
      <a href="#">HOME</a>
      <a href="#">ABOUT US</a>
      <a href="#">SERVICES</a>
      <a href="#">ASSESSMENTS</a>
      <a href="#">WORKPLACES</a>
      <a href="#">LINKS</a>
      <a href="#">CONTACT US</a>
    </nav>
  </header>

  <section class="hero" role="img" aria-label="Photograph: silhouette of a family forming a roof shape with their arms against a purple and orange sunset sky">
    <p class="hero-line first">Corvan T Pty Ltd is dedicated</p>
    <p class="hero-line second">to providing quality customer focused service in all its ventures.</p>
  </section>

  <section class="intro">
    <p>Corvan T Pty Ltd is dedicated to providing quality customer focused service in all its ventures. Corvan T core<br>business is workplace training assessment with broader services which include:</p>
    <ul>
      <li>Employer Workplace skills profiling</li>
      <li>Employee skills profiling (Competency Profiling)</li>
      <li>Workplace training and Assessment</li>
      <li>Resume and Curricula Vita compilation</li>
    </ul>
    <p>The business was established in 1996 trading as RSK &amp; Associates and registered as a company<br>(Corvan T) in 2002.&nbsp; Over this time Corvan T trading as RSK &amp; Associates has built a client base Australia<br>wide aligning engineering trades people against the National training agenda therefore enhancing<br>their employment/career opportunities.&nbsp; The company has built a client base of Ex serving Naval<br>engineering members assisting to align military skills to the industrial sector.&nbsp; This has extended to<br>the general engineering public keen to update qualifications and align to the National training agenda<br>in competency terms.</p>
  </section>

  <div class="divider"></div>

  <aside class="contact">
    <div class="contact-name">Corvan T Pty Ltd</div>
    <div class="contact-trade">RSK &amp; Associates</div>
    <address class="contact-details">
      P.O. Box 2856<br>
      Ashmere Heights, Vic. 3184<br>
      T. 03 9555 0142<br>
      F. 03 9555 0187<br>
      M. 0400 555 268<br>
      E. corvant@tealnet.com.au
    </address>
  </aside>

  <footer class="site-footer">
    <svg width="140" height="30" viewBox="0 0 140 30" aria-label="Social links">
      <circle cx="15" cy="15" r="12.5" fill="none" stroke="#fff" stroke-width="2"/>
      <circle cx="51" cy="15" r="12.5" fill="none" stroke="#fff" stroke-width="2"/>
      <circle cx="87" cy="15" r="12.5" fill="none" stroke="#fff" stroke-width="2"/>
      <circle cx="123" cy="15" r="12.5" fill="none" stroke="#fff" stroke-width="2"/>
    </svg>
  </footer>
</div>
</body>
</html>
```